Volunteer Surgical Organization needs a newsletter to report on a recent mission to Ecuador

We need a newsletter designed to report on our recent surgical mission servicing the indigenous Kichwa indian populations of remote areas of Ecuador. We have text describing the villages we visited along with photos of the different areas. We also have pictures of some of the patients we served. The purpose of the newsletter is to provide a feel about what we did to the donors who supported our trip. We also hope it will inspire other people to donate to support our future mission trips. It must look professional and we have a logo that will be included as well. We like deeper blue and green and yellow colors. Our website is Bright Lantern Overseas and our mission involves ALTRUISM, GLOBAL VOLUNTEERISM, AND COMPASSION. " Bright Lantern Overseas" and the three mission statement words must be included prominently on the newsletter. A request to visit our website and make a donation should also be included.

Target Market(s)

Donors and potential donors

Industry/Entity Type

Non Profit

Font styles to use
Serif

Colors
0555a3
9bcb3c
fbed22
ffffff

Requirements
Must have
• 1. Our Logo.
• 2. Our organization name "Bright Lantern Overseas"
• 3. The three words "Global Volunteerism", " Altruism", "Compassion"
• 4. The organizations URL "www.brightlanternoverseas"
• 5. A request to visit our website and make a donation
• 6. One sheet, both sides
Nice to have
• Sharp, color design with professional font
• Professional look- we have used Word and Pages in the past and it looks so unprofessional
Should not have
• No cartoons, no comics, no cursive fonts

```html
<!DOCTYPE html>
<html lang="en">
<head>
<meta charset="utf-8">
<title>Bright Lantern Overseas – Ecuador Mission Newsletter</title>
<link href="https://fonts.googleapis.com/css2?family=Arimo:wght@400;700&display=swap" rel="stylesheet">
<style>
  :root {
    --page-bg: #d9dada;
    --card-bg: #ffffff;
    --brand-blue: #0555a3;
    --brand-green: #3d7a1e;
    --text-grey: #5a5a5a;
    --muted-grey: #777777;
    --rule-grey: #cfcfcf;
    --social-blue: #2b63ad;
    --social-sky: #1b9ce5;
    --social-navy: #0e6aa7;
  }
  * { margin: 0; padding: 0; box-sizing: border-box; }
  html, body { width: 1200px; height: 2651px; overflow: hidden; }
  body {
    background: var(--page-bg);
    font-family: "Arimo", Arial, sans-serif;
    color: var(--text-grey);
    position: relative;
  }
  .preheader {
    position: absolute; top: 104px; left: 0; width: 1200px;
    text-align: center; font-size: 16px; color: #444;
  }
  .preheader a { color: #5a2a6a; text-decoration: underline; }
  .newsletter {
    position: absolute; left: 193px; top: 152px; width: 814px; height: 2415px;
    background: var(--card-bg);
    border-top: 5px solid var(--brand-blue);
    box-shadow: 0 30px 30px -22px rgba(0,0,0,0.35);
  }
  .abs { position: absolute; }
  .brand {
    left: 0; top: 120px; width: 814px;
    display: flex; justify-content: center; align-items: center; gap: 14px;
  }
  .brand-dot { width: 26px; height: 26px; border-radius: 50%; background: var(--brand-blue); }
  .brand-name { font-weight: 700; font-size: 30px; color: var(--brand-green); letter-spacing: 0.5px; }
  .mission-words {
    left: 0; top: 170px; width: 814px; text-align: center;
    font-size: 13px; letter-spacing: 2px; color: #333;
  }
  .social { display: flex; justify-content: center; gap: 10px; width: 814px; left: 0; }
  .social span { width: 38px; height: 38px; border-radius: 50%; display: block; }
  .social--outline { top: 238px; }
  .social--outline span { border: 2px solid #8a8a8a; }
  .social--solid { top: 2250px; }
  .headline {
    left: 81px; top: 603px; width: 650px;
    color: var(--brand-blue); font-weight: 700; font-size: 16.5px; line-height: 26px;
  }
  .body-copy { font-size: 16px; line-height: 25.7px; color: var(--text-grey); }
  .body-copy strong { color: var(--brand-blue); }
  .rule { left: 31px; width: 752px; height: 1px; background: var(--rule-grey); }
  .faces-title {
    left: 0; width: 814px; top: 1962px; text-align: center;
    color: var(--brand-blue); font-weight: 700; font-size: 20px; line-height: 29px;
  }
  .site-url { left: 0; width: 814px; top: 2308px; text-align: center; font-size: 15px; color: #555; }
  .footer-rule { left: 282px; width: 250px; top: 2337px; height: 1px; background: var(--rule-grey); }
  .copyright { left: 0; width: 814px; top: 2352px; text-align: center; font-size: 15px; font-weight: 700; color: var(--muted-grey); }
  .donate { left: 0; width: 814px; top: 2382px; text-align: center; font-size: 14px; color: var(--brand-blue); }
</style>
</head>
<body>
  <p class="preheader">For anything about this mail you can contract us by <a href="#">click this link.</a></p>

  <main class="newsletter">
    <div class="abs brand">
      <span class="brand-dot"></span>
      <span class="brand-name">Bright Lantern Overseas</span>
    </div>
    <p class="abs mission-words">ALTRUISM · GLOBAL VOLUNTEERISM · COMPASSION</p>

    <div class="abs social social--outline"><span></span><span></span><span></span></div>

    <div class="abs" role="img" aria-label="Village road in the Andes with a llama, small houses and a white pickup truck"
      style="left:31px;top:313px;width:550px;height:258px;background:linear-gradient(180deg,#8a8f86 0%,#6f7a55 45%,#4f5a35 100%);"></div>
    <div class="abs" role="img" aria-label="Green mountain slopes with grazing sheep"
      style="left:595px;top:313px;width:189px;height:258px;background:linear-gradient(180deg,#c9ccce 0%,#7f8a6a 35%,#4d5630 100%);"></div>

    <h1 class="abs headline">THE BRIGHT LANTERN OVERSEAS TEAM PARTNERS AGAIN WITH WILLOW PATH HEALTH TO PROVIDE SPECIALTY SURGICAL CARE TO THE INDIGENT MESTIZOS PEOPLE OF THE SMALL VILLAGES OF GUANGAJE AND OCHO DE SEPTIEMBRE, ECUADOR.</h1>

    <div class="abs" role="img" aria-label="Pink village church with a bell tower under a cloudy sky"
      style="left:31px;top:752px;width:258px;height:185px;background:linear-gradient(180deg,#c7cbcf 0%,#b9a6a8 55%,#6f7664 100%);"></div>
    <div class="abs" role="img" aria-label="White two-storey health center building with parked cars"
      style="left:31px;top:948px;width:258px;height:185px;background:linear-gradient(180deg,#c9cdd1 0%,#d8d8d4 50%,#7a7d78 100%);"></div>
    <p class="abs body-copy" style="left:308px;top:748px;width:460px;">The town of Guangaje was established in 1861. It has historically been known for being farmland belonging to various private and government estates. The population, being 95% indigenous, used to work for such estates until they themselves became landowners. It presently has a population of 7,341, but to date, lacks basic services like potable water, sewage systems, advanced educational programs, and in some areas, electricity. It does have a Health Center and a church, St. John the Baptist. The BLO Team worked with Willow Path and the Health Center, treating a variety of surgical conditions amongst the villagers. The mission of Willow Path Health is to expand access to healthcare services to people in remote villages like we visited and then partner with volunteer organizations like BLO to provide specialty care.</p>

    <div class="abs" role="img" aria-label="Village school building with murals painted along its front wall and a parked truck"
      style="left:31px;top:1168px;width:753px;height:276px;background:linear-gradient(180deg,#a9b0b2 0%,#5f6f6a 50%,#8d8a78 80%,#4c5048 100%);"></div>
    <p class="abs body-copy" style="left:35px;top:1474px;width:745px;">The village of <strong>Ocho de Septiembre</strong> is about 90 minutes away from Latacunga.&nbsp; This primarily farming community has a population of about 600 indigenous Kichwa Indians.&nbsp; The village lacks basic services and has one small school.&nbsp; The BLO Team visited the village and set up a makeshift exam/consultation room in one of the classrooms.&nbsp; We were able to see and treat the villagers, many seeing a surgeon for the first time.</p>

    <div class="abs rule" style="top:1614px;"></div>

    <p class="abs body-copy" style="left:31px;top:1684px;width:460px;">The Hospital Provincial Central De Latacunga is the largest public healthcare facility in the city of Latacunga. Patients from surrounding towns and villages like Guangaje and Ocho de Septiembre travel there for care. The Director of Surgery, Dr. Mateo Ruales and his staff welcomed the BLO Team to the hospital, providing a venue for us to care for our patients.</p>
    <div class="abs" role="img" aria-label="Provincial hospital building in yellow with a palm tree in front"
      style="left:510px;top:1634px;width:274px;height:273px;background:linear-gradient(180deg,#c6cbcf 0%,#c7b98a 45%,#6d7a5a 80%,#4f5a45 100%);"></div>

    <div class="abs rule" style="top:1940px;"></div>

    <h2 class="abs faces-title">The faces of some of the many patients the BLO Team had the privilege<br>to meet and help during our week-long mission.</h2>

    <div class="abs" role="img" aria-label="Smiling patient in a surgical cap resting in a hospital bed"
      style="left:35px;top:2036px;width:300px;height:192px;background:linear-gradient(160deg,#d2a33a 0%,#6b8fb8 50%,#3f6ea8 100%);"></div>
    <div class="abs" role="img" aria-label="Young patient in a hospital bed with a family member beside"
      style="left:344px;top:2036px;width:131px;height:192px;background:linear-gradient(160deg,#9b8a80 0%,#d8d2d4 55%,#b7a6b0 100%);"></div>
    <div class="abs" role="img" aria-label="Volunteer surgeons talking with a patient in a hospital ward"
      style="left:484px;top:2036px;width:300px;height:192px;background:linear-gradient(160deg,#c9c8c4 0%,#8b8d94 50%,#5b5f73 100%);"></div>

    <div class="abs social social--solid">
      <span style="background:var(--social-blue);"></span>
      <span style="background:var(--social-sky);"></span>
      <span style="background:var(--social-navy);"></span>
    </div>

    <p class="abs site-url">www.BRIGHTLANTERNOVERSEAS.com</p>
    <div class="abs footer-rule"></div>
    <p class="abs copyright">© brightlanternoverseas 2017.All right reserved by the Company.</p>
    <p class="abs donate">Please visit our website and make a donation to support our next mission.</p>
  </main>
</body>
</html>
```